Project Management - Web Design Project

Vantrel 4 Management Limited is a company which provides specialist Project Control and Contract Management expertise to the Engineering, Construction and Manufacturing industries. The emphasis is on advanced Project Management techniques in particular Planning & Scheduling, Cost Control, Change Control, Risk Management, Reporting and Contract Administration. We are a global company (albeit a small start-up at this time) and pride ourselves on our ability to support projects to help them achieve their goals and objectives. Our aim is to implement work class control tools in a simple and user friendly manner. We would like the website to appear professional but at the same time easy to navigate and a good balance between text and pictures. The final design should communicate our value added service to our customers, our willingness to support and our structured approach to our work.

Target Market(s)

Project Management professionals working for engineering, construction and manufacturing organisations involved with delivering projects.

Industry/Entity Type

Construction

Requirements
Must have
• The website must include all of the content from the attached Excel brief. The company logo (attached) must also be included in the design. The design must portray a professional look and feel. Please include pictures and photographs related to project management in the engineering, construction and manufacturing industries. We may supplement with pictures of our own during the next steps.
Nice to have
• Emphasis that Vantrel 4 is available to support, guide, direct to achieve positive outcomes for the projects. We work hard at developing our customer relationships. Our employees are experienced in advanced project management techniques.
Should not have
• The design should not use old style fonts. It should look modern and professional. Do not include cartoons or silly illustrations.

```html
<!DOCTYPE html>
<html lang="en">
<head>
<meta charset="utf-8">
<title>Vantrel 4 Management Limited</title>
<link rel="stylesheet" href="https://fonts.googleapis.com/css2?family=Questrial&family=Arimo:wght@400;700&display=swap">
<style>
:root{
  --bg:#0b2440;
  --bg-deep:#071a30;
  --nav:#0e2a47;
  --rule:#2e4a66;
  --accent:#1a7fe6;
  --accent-bright:#2f95ff;
  --text:#ffffff;
  --muted:#8ea3b8;
  --logo-grey:#8d99a6;
  --brand-grey:#56697c;
  --footer:#0d2d4d;
  --social:#2b93a6;
}
*{margin:0;padding:0;box-sizing:border-box}
html,body{width:1175px;height:1200px;overflow:hidden}
body{background:radial-gradient(circle at 12% 4%,#123559 0,var(--bg) 380px) var(--bg);font-family:"Arimo",Arial,sans-serif;color:var(--text);position:relative}
.header{position:absolute;left:0;top:0;width:1175px;height:197px}
.logo{position:absolute;left:58px;top:32px;width:190px}
.logo-mark{width:80px;height:80px;border-radius:50%;background:var(--logo-grey);margin-left:46px}
.logo-name{font-family:"Questrial",sans-serif;color:var(--logo-grey);font-size:30px;letter-spacing:2px;margin-top:8px;line-height:1}
.logo-sub{font-family:"Questrial",sans-serif;color:var(--logo-grey);font-size:11px;letter-spacing:2px;margin-top:2px}
.social-top{position:absolute;left:677px;top:31px;display:flex;gap:15px}
.social-top span{width:34px;height:34px;border-radius:5px;background:var(--social);font-size:7px;display:flex;align-items:center;justify-content:center;color:#0b2a3a;font-family:"Questrial",sans-serif;overflow:hidden;white-space:nowrap}
.search{position:absolute;left:870px;top:31px;width:256px;height:35px;border:1px solid #2a4766;border-radius:5px;background:#0a2038}
.search svg{position:absolute;right:14px;top:7px}
.login{position:absolute;left:1054px;top:158px;width:82px;height:26px;background:#0a1e33;border:1px solid #2a4766;color:#08131f;font-family:"Questrial",sans-serif;font-size:16px;text-align:center;line-height:24px}
.nav{position:absolute;left:105px;top:197px;width:1032px;height:76px;background:var(--nav);border-top:5px solid var(--rule);border-bottom:5px solid var(--rule);display:flex;align-items:center}
.nav a{color:var(--text);text-decoration:none;font-size:13px;padding:0 11px;line-height:44px;border-right:1px solid #061628;white-space:nowrap}
.nav a:last-child{border-right:0}
.nav a.active{color:var(--accent-bright);font-weight:700}
.hero{position:absolute;left:0;top:273px;width:1175px;height:452px;background:linear-gradient(180deg,var(--bg) 0%,#1c4a73 45%,#3a6f98 75%,#102c48 100%)}
.hero-copy{position:absolute;left:539px;top:32px}
.hero h1{font-family:"Questrial",sans-serif;font-weight:400;font-size:29px;line-height:35px}
.hero h1 em{font-style:normal;color:var(--accent-bright);display:block;font-size:31px}
.checks{list-style:none;margin-top:9px}
.checks li{font-family:"Questrial",sans-serif;font-size:17px;height:29px;display:flex;align-items:center;gap:10px}
.btn-more{display:inline-flex;align-items:center;gap:14px;margin:12px 0 0 32px;padding:0 6px 0 16px;height:29px;border-radius:15px;background:linear-gradient(#f2f2f2,#a9a9a9);color:#333;font-family:"Questrial",sans-serif;font-size:15px}
.btn-more i{width:16px;height:16px;border-radius:50%;background:var(--accent);color:#fff;font-style:normal;font-size:14px;line-height:16px;text-align:center}
.welcome{position:absolute;left:106px;top:755px;width:665px}
.welcome h2,.testimonials h2{font-family:"Questrial",sans-serif;font-weight:400;color:var(--accent-bright);font-size:27px}
.welcome p{font-size:11.6px;line-height:14px;margin-top:14px}
.welcome h2+p{margin-top:26px}
a.more{color:var(--accent-bright)}
.testimonials{position:absolute;left:788px;top:741px;width:292px;height:214px;border-radius:8px;background:linear-gradient(#06172a,#0a2340);padding:16px 14px}
.testimonials h2{font-size:28px}
.testimonials p{font-size:10px;line-height:12.4px;margin-top:14px}
.testimonials .more{display:block;margin-top:24px;font-size:10px}
.clients{position:absolute;left:106px;top:996px;width:940px;display:flex;justify-content:space-between;align-items:center;height:40px}
.clients span{font-family:"Arimo",sans-serif;font-weight:700;color:var(--brand-grey);font-size:24px}
.footer{position:absolute;left:0;top:1091px;width:1175px;height:109px;background:var(--footer);border-top:2px solid #24476b}
.follow{position:absolute;top:38px;display:flex;align-items:center;gap:9px;font-size:10px;color:var(--muted)}
.follow b{width:24px;height:24px;border-radius:4px;background:#c7d8e6;display:block}
.legal{position:absolute;left:707px;top:44px;font-size:10px;color:var(--muted)}
.legal nav{display:flex;gap:18px;margin-left:21px}
.legal nav a{color:var(--muted)}
.legal p{margin-top:10px}
</style>
</head>
<body>
<header class="header">
  <div class="logo">
    <div class="logo-mark"></div>
    <div class="logo-name">VANTREL4</div>
    <div class="logo-sub">MANAGEMENT LIMITED</div>
  </div>
  <div class="social-top">
    <span>Feed</span><span>Friend</span><span>Chatter</span><span>View</span>
  </div>
  <div class="search">
    <svg width="24" height="22" viewBox="0 0 24 22"><circle cx="9" cy="9" r="7" fill="none" stroke="#fff" stroke-width="3"/><line x1="14" y1="14" x2="21" y2="20" stroke="#fff" stroke-width="4" stroke-linecap="round"/></svg>
  </div>
  <div class="login">LOGIN</div>
</header>

<nav class="nav">
  <a class="active">HOME</a><a>ABOUT US</a><a>INTRODUCTION</a><a>PROJECT CONTROL</a><a>CONTRACT MANAGEMENT</a><a>SPECIALIST SERVICES</a><a>REFERENCE PROJECT</a><a>CONTACT US</a>
</nav>

<section class="hero" role="img" aria-label="City skyline at night in blue tones">
  <div class="hero-copy">
    <h1>We offer enterprise class operations<em>&amp; Process Management Consulting</em></h1>
    <ul class="checks">
      <li><svg width="24" height="22" viewBox="0 0 24 22"><path d="M2 12l7 8L22 2" fill="none" stroke="#1a7fe6" stroke-width="4"/></svg>Engineering Earned Value</li>
      <li><svg width="24" height="22" viewBox="0 0 24 22"><path d="M2 12l7 8L22 2" fill="none" stroke="#1a7fe6" stroke-width="4"/></svg>Critical Issues Reporting</li>
      <li><svg width="24" height="22" viewBox="0 0 24 22"><path d="M2 12l7 8L22 2" fill="none" stroke="#1a7fe6" stroke-width="4"/></svg>Management Schedules</li>
      <li><svg width="24" height="22" viewBox="0 0 24 22"><path d="M2 12l7 8L22 2" fill="none" stroke="#1a7fe6" stroke-width="4"/></svg>Coaching / Mentoring / Training</li>
    </ul>
    <span class="btn-more">READ MORE <i>+</i></span>
  </div>
</section>

<section class="welcome">
  <h2>Welcome to The Vantrel 4 Management Limited..</h2>
  <p>At Vantrel 4 Management Limited we value our relationship with all of our customers. We are committed to providing value for money solutions within agreed timeframes. We have a reputation for communicating openly and honestly and are prepared to report contensious issues when we believe it is in the best interest of the project. Our employees are highly skilled, motivated and mobile and are trained to act as mentors and coaches to ensure the project team is able to develop this expertiese in-house..</p>
  <p>At Vantrel 4 Management Limited we value our relationship with all of our customers... <a class="more">Learn More</a></p>
</section>

<aside class="testimonials">
  <h2>Client Testimonials</h2>
  <p>Vantrel 4 Management Limited is a company which provides specialist Project Control and Contract Management expertise to the Engineering, Construction and Manufacturing industries. The emphasis is on advanced Project Management techniques in particular Planning &amp; Scheduling,</p>
  <a class="more">Learn More</a>
</aside>

<div class="clients">
  <span>KORVANE</span><span>MERIDEX</span><span>talvio</span><span>QUINTRA</span><span>Brightsoft</span><span>NORLEX</span><span>NETVALE</span>
</div>

<footer class="footer">
  <div class="follow" style="left:128px"><b></b>Follow on Chatterly</div>
  <div class="follow" style="left:277px"><b></b>Become a Fan on Friendbook</div>
  <div class="follow" style="left:474px"><b></b>Watch vedios on ViewStream</div>
  <div class="legal">
    <nav><a>Privacy Policy</a><span>I</span><a>Terms &amp; Conditions</a><span>I</span><a>Contact Us</a></nav>
    <p>@ Copyright Vantrel4 Menegement Limited.&nbsp; 2012&nbsp; All rights reserved</p>
  </div>
</footer>
</body>
</html>
```